Stationery Design Project

KT7 Staffing requires letterhead and business card designs for a company based in London. Just like the name, we're a management resourcing company, providing resources to third party companies. You can see www.kt7staffing-example.com for ideas on existing colour schemes and design concepts that have been implimented and agreed to. Ultimately the design should broadcast professionalism, safety and the concept of growth.

Target Market(s)

Financial institutes; friendly societies (All UK based)

Industry/Entity Type

Safety

Requirements
Must have
• Files produced should be print ready; and the text in them editable (eg address, name etc)

```html
<!DOCTYPE html>
<html lang="en">
<head>
<meta charset="utf-8">
<title>KT7 Staffing – Stationery</title>
<link href="https://fonts.googleapis.com/css2?family=Arimo:wght@400;700&display=swap" rel="stylesheet">
<style>
  :root {
    --teal: #2a9db0;
    --teal-light: #7cc8d4;
    --ink: #111111;
    --paper: #ffffff;
    --backdrop: #ececec;
    --edge: #d4d4d4;
  }
  * { box-sizing: border-box; margin: 0; padding: 0; }
  html, body { width: 1200px; height: 627px; overflow: hidden; }
  body {
    background: linear-gradient(90deg, #e6e6e6 0%, #f7f7f7 60%, #efefef 100%);
    font-family: "Arimo", Arial, sans-serif;
    color: var(--ink);
    position: relative;
  }

  /* Letterhead */
  .letterhead {
    position: absolute; left: 178px; top: 34px;
    width: 373px; height: 559px;
    background: var(--paper);
    border: 1px solid var(--edge);
  }
  .brand {
    display: flex; align-items: center; gap: 6px;
    color: var(--teal); font-weight: 700;
  }
  .brand-mark { width: 9px; height: 9px; background: var(--teal); }
  .letterhead .brand { position: absolute; left: 22px; top: 22px; font-size: 15px; }
  .letterhead-footer {
    position: absolute; left: 18px; right: 18px; bottom: 20px;
    border-top: 2px solid var(--teal-light);
    padding-top: 12px;
    text-align: center; color: var(--teal);
    font-size: 9.5px; line-height: 15px;
  }
  .letterhead-footer strong { font-weight: 700; }
  .letterhead-footer .phones span + span { margin-left: 18px; }

  /* Business cards */
  .card {
    position: absolute; top: 120px;
    width: 230px; height: 350px;
    background: var(--paper);
    border: 1px solid var(--edge);
    border-radius: 14px;
    box-shadow: 0 2px 6px rgba(0,0,0,0.08);
  }
  .card-front { left: 650px; }
  .card-back { left: 920px; }
  .card .mark { position: absolute; left: 22px; top: 24px; }
  .person { position: absolute; left: 22px; top: 80px; }
  .person-name { font-weight: 700; font-size: 13px; text-transform: uppercase; }
  .person-role { font-size: 11px; margin-top: 2px; }
  .contact-list {
    display: grid; grid-template-columns: 44px auto;
    font-size: 10.5px; line-height: 13px; margin-top: 16px;
  }
  .company { position: absolute; left: 22px; bottom: 24px; }
  .company .brand { font-size: 13px; margin-bottom: 10px; }
  .company-name { font-weight: 700; font-size: 11px; }
  .company-address { font-size: 10.5px; margin-bottom: 12px; }
  .company .contact-list { margin-top: 0; }
  .web { font-weight: 700; }
</style>
</head>
<body>

  <section class="letterhead" aria-label="Letterhead">
    <div class="brand"><span class="brand-mark"></span>KT7 Staffing</div>
    <footer class="letterhead-footer">
      <div><strong>KT7 Staffing,</strong> 14 Harrow Court, London, W9 2XY</div>
      <div class="phones"><span>+44 (0) 20 7946 0123</span><span>+44 (0) 7700 900 456</span></div>
      <div><strong>www.kt7staffing-example.com</strong></div>
    </footer>
  </section>

  <section class="card card-front" aria-label="Business card front">
    <span class="brand-mark mark"></span>
    <div class="person">
      <div class="person-name">Dana Whitfield</div>
      <div class="person-role">Graphic Designer</div>
      <div class="contact-list">
        <span>Direct</span><span>+44 (0) 20 7946 0123</span>
        <span>Mob</span><span>+44 (0) 7700 900 456</span>
        <span>Email</span><span>dana.w@example.com</span>
      </div>
    </div>
    <div class="company">
      <div class="brand"><span class="brand-mark"></span>KT7 Staffing</div>
      <div class="company-name">KT7 Staffing</div>
      <div class="company-address">14 Harrow Court, London, W9 2XY</div>
      <div class="contact-list">
        <span>Main</span><span>+44 (0) 20 7946 0123</span>
        <span>Fax</span><span>+44 (0) 7700 900 456</span>
        <span>Web</span><span class="web">kt7staffing-example.com</span>
      </div>
    </div>
  </section>

  <section class="card card-back" aria-label="Business card back">
    <span class="brand-mark mark"></span>
    <div class="company">
      <div class="brand"><span class="brand-mark"></span>KT7 Staffing</div>
      <div class="company-name">KT7 Staffing</div>
      <div class="company-address">14 Harrow Court, London, W9 2XY</div>
      <div class="contact-list">
        <span>Main</span><span>+44 (0) 20 7946 0123</span>
        <span>Fax</span><span>+44 (0) 7700 900 456</span>
        <span>Web</span><span class="web">kt7staffing-example.com</span>
      </div>
    </div>
  </section>

</body>
</html>
```